Fresh-Up our Master Presentation

We are looking for someone who can revise our main presentation and make it more attractive. The previous layout and the slides are uploaded here and need to be revised. You are welcome to work with icons etc. here. The goal is to make it look a little more creative and modern. Brisk Otter is a company from the creative industry and therefore it would be great if it also shows this.

Target Market(s)

B2B

Industry/Entity Type

Communication and Content Creation

Font styles to use
Sans Serif

```html
<!DOCTYPE html>
<html lang="de">
<head>
<meta charset="utf-8">
<title>Brisk Otter – Präsentation</title>
<link href="https://fonts.googleapis.com/css2?family=Open+Sans:wght@400;600;700;800&display=swap" rel="stylesheet">
<style>
:root{
  --navy:#2b3450;
  --orange:#f08a1c;
  --slide:#f1f1f1;
  --text:#3a3f4f;
  --muted:#6b7080;
  --white:#ffffff;
}
*{margin:0;padding:0;box-sizing:border-box}
html,body{width:1200px;height:4196px;overflow:hidden;background:#e6e6e6}
body{position:relative;font-family:"Open Sans",Arial,sans-serif;color:var(--text)}
.slide{position:absolute;left:24px;width:1152px;background:var(--slide);overflow:hidden}
.abs{position:absolute}

/* brand */
.brand{position:absolute;display:flex;align-items:center;gap:12px;color:var(--navy);font-weight:700}
.brand-dot{border-radius:50%;background:var(--navy);flex:none}
.brand-sm{right:30px;font-size:24px}
.brand-sm .brand-dot{width:30px;height:30px}

/* headers and bands */
.header-bar{position:absolute;left:0;top:36px;height:48px;width:880px;background:var(--navy);display:flex;align-items:center;padding-left:92px;color:var(--white);font-weight:800;font-size:26px;letter-spacing:.5px}
.header-badge{position:absolute;left:14px;top:26px;width:68px;height:68px;border-radius:50%;background:var(--white);border:5px solid var(--navy)}
.stripes{position:absolute;display:flex;gap:6px}
.stripes span{display:block;width:12px;height:100%;background:var(--orange);transform:skewX(-30deg)}
.footer-band{position:absolute;bottom:0;height:40px;background:var(--navy)}

/* title */
.title-slide{top:0;height:672px;background:
  radial-gradient(ellipse at 50% 55%,#f7f4f2 0%,#eae6e3 35%,transparent 70%),
  linear-gradient(115deg,#e2622a 0%,#f2a071 28%,#e9ddd6 50%,#b9c7d3 72%,#557693 100%)}
.title-slide .brand{left:50%;transform:translateX(-50%);top:80px;font-size:72px;gap:20px}
.title-slide .brand-dot{width:100px;height:100px}
.welcome{position:absolute;top:392px;width:100%;text-align:center;color:var(--navy);font-weight:800;font-size:50px;letter-spacing:1px}
.welcome-sub{position:absolute;top:494px;width:100%;text-align:center;color:var(--navy);font-weight:700;font-size:24px;letter-spacing:.5px}

/* about */
.about{top:688px;height:672px}
.photo{position:absolute}
.about .photo-back{position:absolute;left:80px;top:140px;width:464px;height:470px;background:var(--orange)}
.about .photo{left:96px;top:124px;width:464px;height:470px;background:linear-gradient(160deg,#9aa7b8,#cfd3d8 45%,#6a6f78)}
.person-name{position:absolute;color:var(--navy);font-weight:800;line-height:1.2}
.about .person-name{left:610px;top:132px;font-size:34px}
.bullets{position:absolute;list-style:none}
.bullets li{position:relative;padding-left:28px;font-size:18px;line-height:1.5;color:var(--text);margin-bottom:24px}
.bullets li::before{content:"";position:absolute;left:0;top:8px;width:14px;height:14px;border-radius:50%;background:var(--orange)}
.about .bullets{left:610px;top:244px;width:500px}

/* community */
.community{top:1380px;height:660px}
.hub{position:absolute;left:476px;top:200px;width:200px;height:200px;border-radius:50%;border:6px solid var(--orange);background:var(--white)}
.hub::after{content:"";position:absolute;inset:22px;border-radius:50%;background:#d9dadf}
.item{position:absolute;width:260px}
.item h3{font-size:19px;font-weight:700;color:var(--navy);margin-bottom:6px}
.item p{font-size:12px;line-height:1.45;color:var(--muted)}
.item.right{text-align:left}
.avatar{position:absolute;width:70px;height:70px;border-radius:50%}

/* social */
.social{top:2060px;height:668px}
.phone{position:absolute;width:190px;height:390px;border-radius:28px;border:8px solid #1c2233}
.social .person-name{font-size:32px}
.social .bullets{width:300px}
.social .bullets li{font-size:17px;margin-bottom:18px}

/* video */
.video{top:2760px;height:664px}
.video-text{position:absolute;left:90px;top:128px;width:972px;text-align:center;font-size:23px;line-height:1.5;color:var(--text)}
.thumb{position:absolute;top:340px;height:190px;border-radius:4px}

/* thanks */
.thanks{top:3464px;height:732px}
.thanks .photo{left:0;top:0;width:576px;height:732px;background:linear-gradient(170deg,#e7d3bd,#c7a98a 45%,#8f7a66)}
.thanks .brand{left:616px;top:64px;font-size:56px;gap:16px}
.thanks .brand-dot{width:76px;height:76px}
.thank-title{position:absolute;left:616px;top:190px;font-size:84px;font-weight:800;color:var(--navy);letter-spacing:1px}
.thank-sub{position:absolute;left:616px;top:300px;font-size:22px;font-weight:700;color:var(--navy)}
.contact{position:absolute;left:616px;display:flex;align-items:center;gap:16px;font-size:22px;font-weight:700;color:var(--navy)}
.socials{position:absolute;left:616px;top:500px;display:flex;gap:18px}
.socials span{width:46px;height:46px;border-radius:50%;border:2px solid #8fb3d9}
.copyright{position:absolute;left:616px;top:620px;font-size:15px;font-weight:700;color:var(--navy)}
</style>
</head>
<body>

<!-- Title -->
<section class="slide title-slide" role="img" aria-label="Titelfolie mit farbigem Low-Poly-Verlauf von Orange zu Blaugrau">
  <div class="brand"><span class="brand-dot"></span>Brisk Otter</div>
  <div class="welcome">WELCOME TO</div>
  <div class="welcome-sub">INDIVIDUELL JE NACH KUNDE</div>
  <div class="stripes" style="left:0;bottom:0;height:12px"><span></span></div>
</section>

<!-- About -->
<section class="slide about">
  <div class="header-bar">ABOUT US</div>
  <div class="header-badge"></div>
  <div class="stripes" style="left:890px;top:36px;height:48px"><span></span><span></span><span></span></div>
  <div class="brand brand-sm" style="top:43px"><span class="brand-dot"></span>Brisk Otter</div>
  <div class="photo-back"></div>
  <div class="photo" role="img" aria-label="Foto der beiden Moderatoren vor einer Stadtkulisse"></div>
  <h2 class="person-name">JONAS KELLER UND<br>MARCO BRUNNER</h2>
  <ul class="bullets">
    <li>Moderatoren, Podcaster, Social Media Hosts und DJs: Jonas Keller und Marco Brunner sind schweizweit bekannte Persönlichkeiten mit hohem Unterhaltungswert.</li>
    <li>Jonas Keller moderiert seit 20 Jahren und Marco Brunner seit 10 Jahren Morgensendungen, insbesondere von Radio Pulse in der Schweiz. Als Morgenduo «Keller und Brunner», mit dem Podcast «Die Plauderstunde» und mit verschiedenen Social-Media-Formaten wie «Endlich Freitag, wenn...» haben sie sich eine grosse Community aufgebaut.</li>
  </ul>
  <div class="stripes" style="left:236px;bottom:0;height:40px"><span></span><span></span><span></span></div>
  <div class="footer-band" style="left:296px;right:0"></div>
</section>

<!-- Community -->
<section class="slide community">
  <div class="header-bar">DIE COMMUNITY</div>
  <div class="header-badge"></div>
  <div class="stripes" style="left:890px;top:36px;height:48px"><span></span><span></span><span></span></div>
  <div class="brand brand-sm" style="top:43px"><span class="brand-dot"></span>Brisk Otter</div>

  <svg class="abs" style="left:0;top:0" width="1152" height="660" viewBox="0 0 1152 660">
    <g fill="none" stroke="#9aa0ad" stroke-width="2">
      <polyline points="130,150 420,150 476,220"/>
      <polyline points="130,340 476,300"/>
      <polyline points="130,500 420,500 476,380"/>
      <polyline points="1022,150 732,150 676,220"/>
      <polyline points="1022,340 676,300"/>
      <polyline points="1022,500 732,500 676,380"/>
    </g>
    <g fill="var(--navy)">
      <circle cx="480" cy="225" r="8"/><circle cx="476" cy="300" r="8"/><circle cx="480" cy="375" r="8"/>
      <circle cx="672" cy="225" r="8"/><circle cx="676" cy="300" r="8"/><circle cx="672" cy="375" r="8"/>
    </g>
  </svg>
  <div class="hub"></div>

  <div class="avatar" style="left:58px;top:116px;background:linear-gradient(135deg,#c56a3a,#2b3450)" role="img" aria-label="Rundes Foto zum Thema Radio"></div>
  <div class="item" style="left:150px;top:116px"><h3>Radio</h3><p>Täglich live am Morgen, mit Humor, Musik und aktuellen Themen begleiten die beiden tausende Hörerinnen und Hörer in den Tag.</p></div>
  <div class="avatar" style="left:58px;top:306px;background:linear-gradient(135deg,#d8c2a8,#5a4f48)" role="img" aria-label="Rundes Foto zum Thema Podcast"></div>
  <div class="item" style="left:150px;top:306px"><h3>Podcast</h3><p>Jede Woche eine neue Folge mit Gästen, Geschichten und spontanen Gesprächen, die eine treue und wachsende Hörerschaft begeistern.</p></div>
  <div class="avatar" style="left:58px;top:466px;background:linear-gradient(135deg,#b9a48e,#3b3f4c)" role="img" aria-label="Rundes Foto zum Thema Social Media"></div>
  <div class="item" style="left:150px;top:466px"><h3>Social Media</h3><p>Kurze Clips, Stories und Serien sorgen auf allen Kanälen für hohe Reichweite, starke Interaktion und viele geteilte Momente.</p></div>

  <div class="item right" style="left:744px;top:116px"><h3>Live-Moderation</h3><p>Ob Firmenanlass, Gala oder Festival: Die beiden führen charmant und souverän durch jedes Programm und begeistern das Publikum.</p></div>
  <div class="avatar" style="left:1024px;top:116px;background:linear-gradient(135deg,#3a5fa8,#111a33)" role="img" aria-label="Rundes Foto einer Live-Bühne"></div>
  <div class="item right" style="left:744px;top:306px"><h3>DJ-Auftritte</h3><p>Mit eigenen Sets bringen sie Clubs, Partys und Events zum Tanzen und sorgen für eine ausgelassene Stimmung bis spät.</p></div>
  <div class="avatar" style="left:1024px;top:306px;background:linear-gradient(135deg,#2a2f45,#0d0f18)" role="img" aria-label="Rundes Foto eines DJ-Auftritts"></div>
  <div class="item right" style="left:744px;top:466px"><h3>TV-Moderation</h3><p>Vor der Kamera überzeugen sie mit Spontanität und Witz, ob in Unterhaltungssendungen, Shows oder besonderen Live-Formaten.</p></div>
  <div class="avatar" style="left:1024px;top:466px;background:linear-gradient(135deg,#4a6fc0,#1a2448)" role="img" aria-label="Rundes Foto eines TV-Studios"></div>

  <div class="stripes" style="left:236px;bottom:0;height:40px"><span></span><span></span><span></span></div>
  <div class="footer-band" style="left:296px;right:0"></div>
</section>

<!-- Social -->
<section class="slide social">
  <div class="header-bar">SOCIAL MEDIA-PRÄSENZ</div>
  <div class="header-badge"></div>
  <div class="stripes" style="left:890px;top:36px;height:48px"><span></span><span></span><span></span></div>
  <div class="brand brand-sm" style="top:43px"><span class="brand-dot"></span>Brisk Otter</div>

  <div class="phone" style="left:86px;top:154px;background:linear-gradient(170deg,#d6dbe0,#c98a2e 60%,#6f5a3a)" role="img" aria-label="Smartphone mit Profilfoto von Jonas Keller"></div>
  <h2 class="person-name" style="left:316px;top:162px">JONAS KELLER</h2>
  <ul class="bullets" style="left:316px;top:230px">
    <li>Snapgram: 48'700 Follower</li>
    <li>Friendbook: 29'200 Follower</li>
    <li>Posts zu den Themen Unterhaltung, Sport, Familie</li>
    <li>Auf Snapgram erreichte Konten pro Monat: 78'900</li>
    <li>Erreichte Zielgruppe: 53% Frauen / 46% Männer</li>
  </ul>

  <div class="phone" style="left:616px;top:154px;background:linear-gradient(170deg,#e4e4e4,#8c7d70 55%,#2d2a2a)" role="img" aria-label="Smartphone mit Profilfoto von Marco Brunner"></div>
  <h2 class="person-name" style="left:846px;top:162px">MARCO BRUNNER</h2>
  <ul class="bullets" style="left:846px;top:230px">
    <li>Snapgram: 63'700 Follower</li>
    <li>Friendbook: 29'500 Follower</li>
    <li>Posts zu den Themen Unterhaltung, Motorrad, Sport</li>
    <li>Auf Snapgram erreichte Konten pro Monat: 145'000</li>
    <li>Erreichte Zielgruppe: 56% Frauen / 43% Männer</li>
  </ul>

  <div class="stripes" style="left:236px;bottom:0;height:40px"><span></span><span></span><span></span></div>
  <div class="footer-band" style="left:296px;right:0"></div>
</section>

<!-- Video -->
<section class="slide video">
  <div class="header-bar">CLIPTUBE-CONTENT</div>
  <div class="header-badge"></div>
  <div class="stripes" style="left:890px;top:36px;height:48px"><span></span><span></span><span></span></div>
  <div class="brand brand-sm" style="top:43px"><span class="brand-dot"></span>Brisk Otter</div>
  <p class="video-text">Seit vielen Jahren sind Jonas Keller und Marco Brunner mit höchst erfolgreichen ClipTube-Formaten wie «Endlich Freitag, wenn...», «Rolf &amp; Beni» oder «Mundart für Anfänger» präsent. Ihr ClipTube Channel hat über 17'000 Abonnent*innen! Jonas Keller und Marco Brunner gewannen 2022 zusammen mit dem Social Team von Pulse</p>
  <div class="thumb" style="left:90px;width:300px;background:linear-gradient(135deg,#e2b24a,#b0513b 55%,#3d3b3a)" role="img" aria-label="Vorschaubild einer Videofolge mit den beiden Moderatoren"></div>
  <div class="thumb" style="left:418px;width:316px;background:linear-gradient(180deg,#7fc3ec,#2c8fd0 55%,#e6eef3)" role="img" aria-label="Vorschaubild eines Videos an einem Pool"></div>
  <div class="thumb" style="left:762px;width:300px;background:linear-gradient(160deg,#3a3a3a,#111 60%,#c8c8c8)" role="img" aria-label="Vorschaubild der Sonderausgabe eines Mundart-Formats"></div>
  <div class="stripes" style="left:236px;bottom:0;height:40px"><span></span><span></span><span></span></div>
  <div class="footer-band" style="left:296px;right:0"></div>
</section>

<!-- Thanks -->
<section class="slide thanks">
  <div class="photo" role="img" aria-label="Porträtfoto eines Ansprechpartners mit Brille"></div>
  <div class="brand"><span class="brand-dot"></span>Brisk Otter</div>
  <div class="thank-title">THANK YOU</div>
  <div class="thank-sub">Ich freue mich auf die Zusammenarbeit</div>
  <div class="contact" style="top:372px">
    <svg width="24" height="20" viewBox="0 0 24 20"><rect x="1" y="1" width="22" height="18" rx="2" fill="none" stroke="var(--orange)" stroke-width="2"/><polyline points="1,2 12,11 23,2" fill="none" stroke="var(--orange)" stroke-width="2"/></svg>
    nik@briskotter.ch
  </div>
  <div class="contact" style="top:424px">
    <svg width="24" height="24" viewBox="0 0 24 24"><path d="M6 2h4l2 5-3 2a12 12 0 0 0 6 6l2-3 5 2v4a2 2 0 0 1-2 2A18 18 0 0 1 4 4a2 2 0 0 1 2-2z" fill="none" stroke="var(--orange)" stroke-width="2"/></svg>
    +41 79 000 12 34
  </div>
  <div class="socials"><span></span><span></span><span></span></div>
  <div class="copyright">Copyright © 2023 by Brisk Otter All Rights Reserved</div>
</section>

</body>
</html>
```